Webpage needed for a new legal recruitment/headhunting companyi

I would like a professional and sharp looking website to showcase a new legal headhunting/recruitment company called Ridgel. The logo for the company is attached.

I like the following websites:
http://www.brimvaleadvisory.co.uk/
(For the general style and layout- although photographs of the team will be difficult as we don't have one yet!;-))

http://qomd.co.uk/
I like the style of the photographs etc on this one.

NB the pictures attached below are for information only- I don't think I would be able to use any of them...

Hope you can help!
Many thanks

```html
<!DOCTYPE html>
<html lang="en">
<head>
<meta charset="utf-8">
<title>Ridgel Legal Recruitment</title>
<link rel="stylesheet" href="https://fonts.googleapis.com/css2?family=Open+Sans:wght@400;600&display=swap">
<style>
:root{
  --purple:#4a3a8c;
  --purple-dark:#3b2d73;
  --purple-nav:#5b4cae;
  --purple-light:#6a5cc0;
  --text:#555;
  --text-light:#777;
  --footer:#333;
  --rule:#d4d4d4;
  --yellow:#f3e27a;
}
*{margin:0;padding:0;box-sizing:border-box}
html,body{width:1200px;height:1126px;overflow:hidden}
body{font-family:"Open Sans",Arial,sans-serif;color:var(--text);background:#fff;position:relative}
.abs{position:absolute}
.hero-band{left:0;top:0;width:1200px;height:561px;background:linear-gradient(#fff 0,#fff 400px,#f3f3f3 561px);border-bottom:1px solid #e2e2e2}
.brand{left:101px;top:24px;display:flex;align-items:center;gap:10px}
.brand-mark{width:30px;height:30px;border-radius:50%;background:var(--purple)}
.brand-name{font-size:52px;font-weight:400;color:var(--purple);letter-spacing:1px;line-height:1}
.contact{right:148px;top:34px;text-align:right}
.contact .addr{font-size:13px;color:var(--text-light)}
.contact .phone{font-size:20px;color:#555;margin-top:4px}
.contact .phone b{font-weight:400;color:var(--purple-nav)}
.contact-icon{left:1073px;top:40px}
.nav{left:99px;top:116px;width:1002px;height:48px;background:linear-gradient(var(--purple-light),var(--purple-nav));display:flex;border-bottom:2px solid #4636a0}
.nav a{display:flex;align-items:center;justify-content:center;color:#fff;text-decoration:none;font-size:14px;border-right:1px solid #7a6dcf;height:100%}
.nav a.active{background:var(--purple-dark)}
.search{left:957px;top:123px;width:135px;height:34px;background:#fff;border-radius:3px;display:flex;align-items:center;padding-left:11px;font-size:13px;color:#999}
.search svg{position:absolute;right:8px;top:8px}
.slide-photo{left:99px;top:172px;width:703px;height:341px;background:linear-gradient(#8f8fcc 0,#6c6db0 35%,#2a2a4a 62%,#1a6e7a 82%,#1c3a55 100%)}
.slide-panel{left:802px;top:172px;width:299px;height:341px;background:linear-gradient(#4c3f93,#3c2f7c);color:#fff;padding:60px 18px 0 25px;box-shadow:0 2px 3px rgba(0,0,0,.3)}
.slide-panel h2{font-size:20px;font-weight:400;line-height:27px}
.slide-panel p{font-size:13px;line-height:21px;margin-top:16px;color:#e7e4f5}
.btn{display:inline-block;margin-top:13px;background:#f1f1f1;color:#555;font-size:13px;padding:7px 12px;border-radius:3px}
.dots{left:568px;top:536px;display:flex;gap:6px}
.dots i{width:10px;height:10px;border-radius:50%;background:#9a9a9a}
.dots i:first-child{background:#666}
.welcome{left:101px;top:592px;width:487px}
.welcome h1{font-size:20px;font-weight:400;color:var(--purple)}
.welcome p{font-size:13.5px;line-height:21px;margin-top:9px;color:var(--text)}
.rule{height:1px;background:var(--rule)}
.feature{top:800px;width:225px}
.feature h3{font-size:19px;font-weight:400;color:var(--purple);display:flex;align-items:center;gap:10px;height:32px}
.feature p{font-size:12.5px;line-height:17px;color:var(--text-light);margin-top:6px}
.feature a{display:block;font-size:12.5px;color:var(--purple);margin-top:8px;text-decoration:none}
.news-photo{left:610px;top:596px;width:230px;height:152px;background:linear-gradient(#8aa8c8 0,#5a7a5a 40%,#3aa8b8 70%,#c8c0b8 100%)}
.news-box{left:610px;top:748px;width:230px;height:150px;background:linear-gradient(#1f1f1f,#2f2f2f);color:#fff;padding:12px 14px}
.news-box h3{font-size:20px;font-weight:400;display:flex;justify-content:space-between;align-items:center;padding-bottom:9px;border-bottom:1px solid #555}
.news-box p{font-size:12.5px;line-height:17px;margin-top:11px}
.news-box .date{font-size:12.5px;color:#aaa;margin-top:7px}
.resume-box{left:862px;top:596px;width:230px;height:150px;background:linear-gradient(#5a4cb0,#4a3c98);color:#fff;padding:12px 13px}
.resume-box h3{font-size:20px;font-weight:400;padding-bottom:9px;border-bottom:1px solid #7d70c8}
.resume-box p{font-size:12.5px;line-height:17px;margin-top:10px;padding-left:2px}
.resume-box a{display:block;font-size:12.5px;color:var(--yellow);margin-top:8px;text-decoration:none;padding-left:2px}
.resume-photo{left:862px;top:746px;width:230px;height:152px;background:linear-gradient(135deg,#5a5a5a,#cfcfcf 45%,#eeeeee 70%,#9a9a9a)}
.quote{left:126px;top:963px;display:flex;align-items:center;gap:8px;font-size:21px;color:#444}
.quote .mark{font-size:16px;font-weight:600;color:#555;font-family:Georgia,serif;line-height:1}
.quote .mark.open{align-self:flex-start;margin-top:2px}
.quote .mark.close{align-self:flex-end;margin-bottom:-4px}
.quote .who{font-size:16px;color:var(--purple);margin-left:6px}
.footer{left:0;top:1024px;width:1200px;height:102px;background:var(--footer)}
.footer-links{left:101px;top:1047px;font-size:13px;color:#ccc;display:flex;gap:12px}
.footer-links span{color:#999}
.copyright{left:101px;top:1083px;font-size:12.5px;color:#bbb}
.social{left:970px;top:1062px;display:flex;gap:9px}
.social i{width:25px;height:25px;border-radius:50%;background:#777;display:flex;align-items:center;justify-content:center}
</style>
</head>
<body>
<div class="abs hero-band"></div>

<header>
  <div class="abs brand"><span class="brand-mark"></span><span class="brand-name">Ridgel</span></div>
  <div class="abs contact">
    <div class="addr">12, Harlow House, Mercer Lane, Town - Postcode</div>
    <div class="phone">Call us : <b>651 482 3907</b></div>
  </div>
  <svg class="abs contact-icon" width="28" height="32" viewBox="0 0 28 32" aria-hidden="true">
    <rect x="3" y="1" width="23" height="30" rx="2" fill="#555"/>
    <rect x="0" y="6" width="5" height="3" fill="#555"/><rect x="0" y="14" width="5" height="3" fill="#555"/><rect x="0" y="22" width="5" height="3" fill="#555"/>
    <text x="15" y="21" font-size="13" fill="#fff" text-anchor="middle" font-family="Arial,sans-serif">@</text>
  </svg>
</header>

<nav class="abs nav">
  <a class="active" style="width:93px">HOME</a>
  <a style="width:119px">ABOUT US</a>
  <a style="width:111px">SERVICES</a>
  <a style="width:79px">JOBS</a>
  <a style="width:129px">COMPANIES</a>
  <a style="width:88px">NEWS</a>
  <a style="width:85px">BLOG</a>
  <a style="width:134px">CONTACT US</a>
</nav>
<div class="abs search">Search
  <svg width="18" height="18" viewBox="0 0 18 18" aria-hidden="true"><circle cx="7" cy="7" r="5.5" fill="none" stroke="#999" stroke-width="2"/><line x1="11" y1="11" x2="16" y2="16" stroke="#999" stroke-width="2.5"/></svg>
</div>

<section>
  <div class="abs slide-photo" role="img" aria-label="Night city skyline reflected on water"></div>
  <div class="abs slide-panel">
    <h2>PELLENTESQUE HABITAN MORBI PLACERAT</h2>
    <p>Duis sit amet justo felis. Proin tincidunt viverra purus at adipiscing. Fusce posuere eu ligula pulvinar vestibulum. Etiam rutrum consequat aliquam.</p>
    <span class="btn">Read more</span>
  </div>
  <div class="abs dots"><i></i><i></i><i></i><i></i></div>
</section>

<main>
  <div class="abs welcome">
    <h1>WELCOME TO RIDGEL LEGAL RECRUITMENT</h1>
    <p>Nullam id ultrices ipsum, quis vehicula felis. Praesent at mauris sollicitudin, congue nunc eget, vulputate purus. Nulla vehicula tortor ut leo malesuada, nec iaculis ante blandit. Fusce sed ornare eros, aliquet ullamcorper risus. Curabitur placerat dictum risus, id tincidunt libero porttitor non. Pellen-tesque habitant morbi tristique senectus et netus et malesuada fames ac turpis egestas.</p>
  </div>
  <div class="abs rule" style="left:99px;top:772px;width:489px"></div>

  <div class="abs feature" style="left:101px">
    <h3><svg width="34" height="20" viewBox="0 0 34 20" aria-hidden="true" fill="#4a3a8c"><circle cx="8" cy="6" r="4"/><circle cx="17" cy="5" r="4.5"/><circle cx="26" cy="6" r="4"/><path d="M1 19c0-6 3-8 7-8s7 2 7 8z"/><path d="M19 19c0-6 3-8 7-8s7 2 7 8z"/><path d="M9 19c0-7 4-9 8-9s8 2 8 9z"/></svg>Recent Job List</h3>
    <p>Suspendisse pulvinar magna porttitor lectus hendrerit, at euismod odio.</p>
    <a>READ MORE</a>
  </div>
  <div class="abs feature" style="left:366px">
    <h3><svg width="28" height="32" viewBox="0 0 28 32" aria-hidden="true" fill="#4a3a8c"><circle cx="14" cy="7" r="6"/><path d="M0 32c0-11 6-15 14-15s14 4 14 15z"/></svg>Recent Applicants</h3>
    <p>Suspendisse pulvinar magna porttitor lectus hendrerit, at euismod odio.</p>
    <a>READ MORE</a>
  </div>

  <div class="abs news-photo" role="img" aria-label="Coastal bay with harbour and cruise ship"></div>
  <div class="abs news-box">
    <h3>LATEST NEWS <svg width="18" height="18" viewBox="0 0 18 18" aria-hidden="true"><circle cx="9" cy="9" r="8.5" fill="#888"/><path d="M7 5l5 4-5 4z" fill="#2a2a2a"/></svg></h3>
    <p>Phasellus vestibulum egestas nulla, ut tincidunt augue aliquam vitae pellentesque.</p>
    <div class="date">March 4, 2013</div>
  </div>

  <div class="abs resume-box">
    <h3>RESUME HELP</h3>
    <p>Phasellus vestibulum egestas nulla, ut tincidunt augue aliquam vitae pellentesque.</p>
    <a>CLICK HERE</a>
  </div>
  <div class="abs resume-photo" role="img" aria-label="Curriculum vitae document with pen and glasses"></div>

  <div class="abs rule" style="left:99px;top:935px;width:1002px"></div>
  <blockquote class="abs quote">
    <span class="mark open">&ldquo;</span>
    <span>Cras ut tortor tincidunt, aliquam nulla et, volutpat ante facilisis convallis</span>
    <span class="mark close">&rdquo;</span>
    <span class="who">- &nbsp;Customer name, City</span>
  </blockquote>
</main>

<footer>
  <div class="abs footer"></div>
  <div class="abs footer-links">Home <span>|</span> About us <span>|</span> Services <span>|</span> Jobs <span>|</span> Companies <span>|</span> News <span>|</span> Blog <span>|</span> Contact us</div>
  <div class="abs copyright">Copyright &copy; 2014 &nbsp;Ridgel. &nbsp;All rights reserved.</div>
  <div class="abs social">
    <i></i><i></i><i></i>
    <i><svg width="14" height="10" viewBox="0 0 14 10" aria-hidden="true"><rect x="0.5" y="0.5" width="13" height="9" fill="none" stroke="#333"/><path d="M0.5 0.5l6.5 5 6.5-5" fill="none" stroke="#333"/></svg></i>
  </div>
</footer>
</body>
</html>
```